Events floral designer business needs a logo design

I need a logo design for my floral design business called tender thorns.
i am inspired by nature and the simplicity of its beauty, whilst upcycling and recycling materials to reduce waste and impact on our environment.
I would like the design to be printed on recycled brown cardboard so i would like a simple but striking design of a bold black ivy vine or gnarly magnolia or tree branch with lower case old school type writer font.

Target Market(s)

Anyone requiring floral additions for their event

Industry/Entity Type

Business

Contact Information for Business Card

mara hollis
floral designer/creator
0418657203
mara@tenderthorns.com
tenderthorns.com

Font styles to use
Other font styles liked:
• lower case type writer

Colors
000000

Requirements
Must have
• simplicity but boldness
• Black typewriter font and bold picture with my details
Nice to have
• as above
Should not have
• colour

```html
<!DOCTYPE html>
<html lang="en">
<head>
<meta charset="utf-8">
<title>Tender Thorns – Business Card</title>
<link href="https://fonts.googleapis.com/css2?family=Open+Sans:wght@400;600&display=swap" rel="stylesheet">
<style>
  :root {
    --ink: #111111;
    --paper: #f4f4f4;
    --paper-back: #ffffff;
    --stage: #e6e3e0;
    --text: #1a1a1a;
  }
  html, body {
    margin: 0;
    padding: 0;
    width: 1200px;
    height: 900px;
    overflow: hidden;
    background: var(--stage);
    font-family: "Open Sans", Arial, sans-serif;
  }
  .canvas {
    position: relative;
    width: 1200px;
    height: 900px;
  }
  .card {
    position: absolute;
    overflow: hidden;
    box-shadow: 0 6px 18px rgba(0,0,0,0.18);
  }
  .card-front {
    left: 78px;
    top: 35px;
    width: 588px;
    height: 363px;
    background: var(--paper);
  }
  .vine-panel {
    position: absolute;
    left: 0;
    top: 0;
  }
  .holder-name {
    position: absolute;
    left: 50px;
    top: 52px;
    margin: 0;
    font-size: 20px;
    font-weight: 600;
    letter-spacing: 0.5px;
    color: var(--text);
  }
  .holder-role {
    position: absolute;
    left: 50px;
    top: 79px;
    margin: 0;
    font-size: 15px;
    font-weight: 400;
    color: var(--text);
  }
  .contact-list {
    position: absolute;
    left: 50px;
    top: 248px;
    margin: 0;
    padding: 0;
    list-style: none;
    font-size: 15px;
    color: var(--text);
  }
  .contact-list li {
    display: flex;
    align-items: center;
    height: 21px;
  }
  .contact-icon {
    width: 13px;
    height: 13px;
    margin-right: 6px;
    fill: var(--ink);
  }
  .card-back {
    left: 388px;
    top: 505px;
    width: 566px;
    height: 352px;
    background: var(--paper-back);
  }
  .brand-mark {
    position: absolute;
    left: 224px;
    top: 104px;
    width: 76px;
    height: 76px;
    border-radius: 50%;
    background: var(--ink);
  }
  .brand-name {
    position: absolute;
    left: 0;
    right: 0;
    top: 222px;
    margin: 0;
    text-align: center;
    font-size: 38px;
    font-weight: 600;
    letter-spacing: 3px;
    color: var(--ink);
  }
</style>
</head>
<body>
<main class="canvas">

  <section class="card card-front">
    <svg class="vine-panel" width="588" height="363" viewBox="0 0 588 363" role="img" aria-label="Illustration of a white leafy vine branch on a black panel">
      <defs>
        <linearGradient id="vineTone" x1="0" y1="0" x2="1" y2="0">
          <stop offset="0" stop-color="#d9d9d9"/>
          <stop offset="0.35" stop-color="#111111"/>
          <stop offset="1" stop-color="#111111"/>
        </linearGradient>
      </defs>
      <path d="M386 0 C 470 80, 470 250, 420 363 L 588 363 L 588 0 Z" fill="url(#vineTone)"/>
    </svg>

    <h1 class="holder-name">MARA HOLLIS</h1>
    <p class="holder-role">Floral Designer/Creator</p>

    <ul class="contact-list">
      <li>
        <svg class="contact-icon" viewBox="0 0 24 24"><path d="M6.6 10.8a15.1 15.1 0 0 0 6.6 6.6l2.2-2.2a1 1 0 0 1 1-.25 11.4 11.4 0 0 0 3.6.57 1 1 0 0 1 1 1V20a1 1 0 0 1-1 1A17 17 0 0 1 3 4a1 1 0 0 1 1-1h3.5a1 1 0 0 1 1 1c0 1.25.2 2.45.57 3.6a1 1 0 0 1-.25 1z"/></svg>
        0418657203
      </li>
      <li>
        <svg class="contact-icon" viewBox="0 0 24 24"><path d="M2 5h20v14H2z M3.5 6.5 12 13l8.5-6.5" fill="none" stroke="#111" stroke-width="2.2"/><path d="M2 5h20v2l-10 7L2 7z"/></svg>
        mara@tenderthorns.com
      </li>
      <li>
        <svg class="contact-icon" viewBox="0 0 24 24"><circle cx="12" cy="12" r="10"/><path d="M2 12h20M12 2c3 3 3 17 0 20M12 2c-3 3-3 17 0 20" fill="none" stroke="#f4f4f4" stroke-width="1.5"/></svg>
        www.tenderthorns.com
      </li>
    </ul>
  </section>

  <section class="card card-back">
    <div class="brand-mark" aria-hidden="true"></div>
    <p class="brand-name">TENDER THORNS</p>
  </section>

</main>
</body>
</html>
```